依頼詳細
海外のタブーの配色が分からないのでカラーはおまかせします。
現在、百貨店、道の駅、ホテルにも置かせてもらっています。プレゼントにもいけるぐらいのパッケージがいいと思います。 手に取ってもらえるようなインパクトのあるデザイン、また、和紙と一目で分かるもの、これマスク?という意外性ほしいです。 海外は特に環境にうるさいのでパッケージは箱?紙素材にしたいです。
記載項目
マスクサイズは縦15.5センチ横11センチ折りたたんだサイズです。これにはいるサイズがいいかと思います。
希望イメージ
シンプル 複雑
単色 カラフル
暗い 明るい
日常 高級
遊び心 厳粛
未来的 伝統的
女性的 男性的
希望する色
水色系、緑系、黄・オレンジ系
納品ファイル
• 高解像度JPG (.jpg)
補足説明
日本でも海外でも人気の配色にしてください。タブーの配色が分かりません。
■ 選んだ理由

社員一同多数決で決めました。

■ 提案者全員のお礼・コメント

どのデザインもとても素敵で社員一同かなり悩みました。弊社のために時間を費やしていただき誠にありがとうございました。 今後も新商品も出す予定です。 その時はまたお力を貸して頂きたいです。
よろしくお願い致します

```html
<!DOCTYPE html>
<html lang="ja">
<head>
<meta charset="utf-8">
<title>和紙マスク — tsumugi</title>
<link rel="stylesheet" href="https://fonts.googleapis.com/css2?family=Shippori+Mincho:wght@400;500&family=Courier+Prime&family=Noto+Sans+JP:wght@400&display=swap">
<style>
  :root {
    --paper-light: #f1efe8;
    --paper-mid: #e2ded4;
    --paper-dark: #d6d1c5;
    --panel: #ffffff;
    --ink: #1b1b1b;
    --ink-soft: #3a3a3a;
    --mask-fill: #ecebe6;
  }
  html, body {
    margin: 0;
    padding: 0;
    overflow: hidden;
    background: var(--paper-light);
  }
  .package {
    position: relative;
    width: 850px;
    height: 1200px;
    overflow: hidden;
    background:
      radial-gradient(ellipse at 20% 15%, var(--paper-light) 0%, transparent 60%),
      radial-gradient(ellipse at 80% 85%, var(--paper-dark) 0%, transparent 65%),
      linear-gradient(160deg, var(--paper-light) 0%, var(--paper-mid) 100%);
  }
  .label-panel {
    position: absolute;
    left: 221px;
    top: 0;
    width: 407px;
    height: 1070px;
    background: var(--panel);
  }
  .title {
    position: absolute;
    left: 50%;
    top: 48px;
    transform: translateX(-50%);
    margin: 0;
    writing-mode: vertical-rl;
    font-family: "Shippori Mincho", serif;
    font-weight: 400;
    font-size: 112px;
    line-height: 1;
    letter-spacing: 10px;
    color: var(--ink);
  }
  .subtitle {
    position: absolute;
    left: 0;
    width: 850px;
    top: 684px;
    margin: 0;
    text-align: center;
    font-family: "Courier Prime", monospace;
    font-size: 24px;
    color: var(--ink-soft);
  }
  .mask-illustration {
    position: absolute;
    left: 128px;
    top: 728px;
    width: 594px;
    height: 250px;
    border-radius: 40px;
    background: linear-gradient(180deg, var(--mask-fill) 0%, #f6f5f1 100%);
  }
  .uv-note {
    position: absolute;
    left: 0;
    width: 850px;
    top: 996px;
    margin: 0;
    text-align: center;
    font-family: "Noto Sans JP", sans-serif;
    font-size: 19px;
    color: var(--ink-soft);
  }
  .brand {
    position: absolute;
    left: 0;
    width: 850px;
    top: 1094px;
    display: flex;
    justify-content: center;
    align-items: center;
    gap: 22px;
  }
  .brand-square {
    width: 48px;
    height: 48px;
    border: 2px solid var(--ink-soft);
    box-sizing: border-box;
  }
  .brand-name {
    font-family: "Courier Prime", monospace;
    font-size: 40px;
    color: var(--ink-soft);
  }
</style>
</head>
<body>
  <main class="package">
    <div class="label-panel"></div>
    <h1 class="title">和紙マスク</h1>
    <p class="subtitle">Japanese paper mask</p>
    <div class="mask-illustration" role="img" aria-label="Line drawing of a pleated washi paper face mask with ear loops"></div>
    <p class="uv-note">紫外線90%以上カット</p>
    <div class="brand">
      <span class="brand-square"></span>
      <span class="brand-name">tsumugi</span>
    </div>
  </main>
</body>
</html>
```